Waste Oil Filter collection & disposal

Basically I need a 1 page website for the business called Grennick Waste Partners.
We are a environmental service provider and we collect and dispose of waste oil filters to protect the environment from hazardous waste oil products.

This is the link to our current website: www.grennickwaste.co.nz

we want it to look fresh and better than our current website. we may potentially look at getting a new logo designed and are open to ideas/designs if you have any.

Industry/Entity Type

Business

Logo Text

Grennick Waste Partners

Number of Pages Required

1 page

Requirements
Must have
• same colours as current website.
• description of what service we provide please refer to leaflet attached

```html
<!DOCTYPE html>
<html lang="en">
<head>
<meta charset="utf-8">
<title>Grennick Waste Partners</title>
<link href="https://fonts.googleapis.com/css2?family=Open+Sans:wght@400;600;700&family=Roboto:wght@400;500;700&display=swap" rel="stylesheet">
<style>
:root{
  --green:#3f8a3c;
  --green-dark:#2f6e2d;
  --ink:#222;
  --body:#777;
  --light:#efefef;
  --footer:#121212;
  --white:#fff;
  --red:#e52d27;
  --navy:#2d4a8a;
}
*{margin:0;padding:0;box-sizing:border-box}
html,body{width:1200px;height:2995px;overflow:hidden;background:var(--white)}
body{position:relative;font-family:'Roboto',Arial,sans-serif;color:var(--ink)}
.abs{position:absolute}
.topline{left:0;top:0;width:1200px;height:4px;background:var(--green)}
.brand{left:100px;top:44px;font-family:'Open Sans',sans-serif;font-weight:700;font-size:17px;color:var(--green);display:flex;align-items:center;gap:10px}
.brand i{display:block;width:34px;height:34px;border-radius:50%;background:var(--green)}
.nav{left:368px;top:54px;display:flex;gap:0;font-size:14px;font-weight:500;color:#222}
.nav span{margin-right:38px}
.social{display:flex;gap:10px}
.social i{display:block;width:34px;height:34px;border-radius:50%}
.hero{left:0;top:118px;width:1200px;height:548px}
.hero-box{left:258px;top:272px;width:686px;height:248px;background:rgba(0,0,0,.72);text-align:center;color:var(--white)}
.hero-box h1{font-family:'Open Sans',sans-serif;font-weight:700;font-size:42px;margin-top:28px;letter-spacing:.5px}
.hero-box p{font-family:'Open Sans',sans-serif;font-size:22px;letter-spacing:3px;margin-top:14px}
.btn-ghost{display:inline-block;margin-top:22px;border:2px solid var(--white);border-radius:4px;padding:10px 20px;font-size:17px;font-weight:500}
.dots{left:564px;top:578px;display:flex;gap:6px}
.dots i{display:block;width:14px;height:14px;border-radius:50%;border:2px solid var(--white)}
.dots i.on{background:var(--white)}
.about-img{left:104px;top:738px;width:316px;height:316px;border-radius:50%;border:4px solid var(--green);background:radial-gradient(circle at 45% 50%,#e8ede8 0,#7fa77b 45%,#2c4a2a 100%)}
h2{font-family:'Open Sans',sans-serif;font-weight:600;font-size:28px;color:#222}
.about h2{margin-bottom:14px}
.about{left:446px;top:740px;width:660px}
.about p{font-size:12.5px;line-height:32px;color:var(--body)}
.btn-pill{display:inline-block;margin-top:26px;border:1px solid #ccc;border-radius:22px;padding:10px 26px;font-size:15px;font-weight:500;color:var(--green)}
.band{left:0;top:1140px;width:1200px;height:186px;background:var(--green)}
.band p{position:absolute;left:98px;top:44px;width:700px;color:var(--white);font-size:23px;font-weight:500;line-height:44px}
.bin{left:830px;top:1168px;width:190px;height:262px;border-radius:14px 14px 8px 8px;background:linear-gradient(#3a3a3a,#151515)}
.process{left:98px;top:1416px}
.process p{font-size:14px;color:var(--body);margin-top:20px}
.step{width:300px;text-align:center}
.step svg{display:block;margin:0 auto}
.step h3{font-size:15px;font-weight:500;color:#222;margin-top:12px;line-height:24px;text-transform:uppercase}
.step p{font-size:12.5px;line-height:25px;color:var(--body);margin-top:10px}
.divider{width:1px;height:130px;background:#ddd}
.reviews{left:0;top:2030px;width:1200px;height:520px;background:var(--light)}
.reviews h2{position:absolute;top:76px;width:100%;text-align:center}
.card{position:absolute;top:150px;width:318px;height:192px;background:var(--white);padding:18px 20px}
.avatar{position:absolute;left:20px;top:18px;width:70px;height:70px;border-radius:50%;background:linear-gradient(#c9b8a8,#6b5a4c)}
.who{position:absolute;left:100px;top:30px;font-size:13px;line-height:20px}
.who em{color:var(--body);font-size:12px}
.badge{position:absolute;right:20px;top:36px;padding:6px 10px;color:var(--white);font-size:11px;font-weight:700;border-radius:2px}
.card .txt{position:absolute;left:20px;top:102px;width:280px;font-size:12.5px;line-height:24px;color:#555}
.card .meta{position:absolute;left:20px;top:158px;font-size:11.5px;color:#444}
.arrow{position:absolute;top:2258px;width:40px;height:40px;border-radius:50%;border:2px solid #ccc}
.footer{left:0;top:2465px;width:1200px;height:530px}
.footer-body{left:0;top:2550px;width:1200px;height:445px;background:var(--footer)}
.col h4{font-size:18px;font-weight:500;color:var(--white);margin-bottom:24px}
.contact li{list-style:none;display:flex;align-items:center;gap:14px;color:var(--white);font-size:12.5px;line-height:20px;margin-bottom:14px}
.contact li i{flex:none;width:36px;height:36px;border-radius:50%;border:1px solid #777;display:flex;align-items:center;justify-content:center}
.links li{list-style:none;color:var(--white);font-size:12.5px;line-height:31px}
.news p{color:var(--white);font-size:12px}
.news .field{margin-top:22px;width:274px;height:42px;background:var(--white);font-size:12px;color:#999;padding:14px 14px}
.news .sub{margin-top:12px;width:120px;height:40px;background:var(--green);color:var(--white);font-size:14px;font-weight:500;text-align:center;line-height:40px}
.foot-brand{left:880px;top:2626px;color:var(--green);font-family:'Open Sans',sans-serif;font-weight:700;font-size:16px;display:flex;align-items:center;gap:10px}
.foot-brand i{display:block;width:30px;height:30px;border-radius:50%;background:var(--green)}
.rule{left:98px;top:2912px;width:1004px;height:1px;background:#444}
.copy{left:0;top:2944px;width:1200px;text-align:center;color:var(--white);font-size:12px}
</style>
</head>
<body>
<div class="abs topline"></div>
<div class="abs brand"><i></i>Grennick Waste Partners</div>
<div class="abs nav"><span>HOME</span><span>MY GALLERY</span><span>ABOUT US</span><span>BLOG</span><span>TESTIMONIALS</span><span>CONTACT US</span>
  <div class="social"><i style="background:#2d4a8a"></i><i style="background:#2a9fd8"></i><i style="background:#e52d27"></i></div>
</div>

<svg class="abs hero" viewBox="0 0 1200 548" role="img" aria-label="City skyline with harbour beyond a grassy park hill">
  <defs><linearGradient id="sky" x1="0" y1="0" x2="0" y2="1">
    <stop offset="0" stop-color="#c9a9b3"/><stop offset=".35" stop-color="#8a8fa3"/><stop offset=".6" stop-color="#6f6a5a"/><stop offset="1" stop-color="#a86a22"/></linearGradient></defs>
  <polygon points="0,0 1200,0 1200,462 600,548 0,462" fill="url(#sky)"/>
  <polygon points="0,462 600,548 1200,462 1200,472 600,548 0,472" fill="var(--green)"/>
  <polygon points="0,462 600,548 1200,462 1200,480 600,548 0,480" fill="var(--green)"/>
</svg>
<div class="abs hero-box"><h1>GRENNICK WASTE PARTNERS</h1><p>KEEPING NEW ZEALAND GREEN</p><span class="btn-ghost">READ MORE</span></div>
<div class="abs dots"><i class="on"></i><i></i><i></i><i></i></div>

<div class="abs about-img" role="img" aria-label="Green and white collection truck"></div>
<div class="abs about">
  <h2>ABOUT GRENNICK WASTE PARTNERS</h2>
  <p>Sed ut perspiciatis unde omnis iste natus error sit voluptatem accusantium doloremque laudantium, totam rem aperiam, eaque ipsa quae ab illo inventore veritatis et quasi architecto beatae vitae dicta sunt explicabo. Nemo enim ipsam voluptatem quia voluptas sit aspernatur aut odit aut fugit, sed quia consequuntur magni dolores eos qui ratione voluptatem sequi nesciunt. Neque porro quisquam est, qui dolorem ipsum quia dolor sit amet, consectetur.<br>Ut enim ad minima veniam, quis nostrum exercitationem ullam corporis suscipit laboriosam, nisi ut aliquid ex ea commodi consequatur enim ad minima veniam, quis nostrum ut aliquid ex ea commodi consequatur.</p>
  <span class="btn-pill">READ MORE ➜</span>
</div>

<div class="abs band"><p>Grennick Waste Partners Ltd service the Lower North Island and specialise in the collection &amp; disposal of oil &amp; fuel filters</p></div>
<div class="abs bin" role="img" aria-label="Black wheelie bin"></div>

<div class="abs process"><h2>THE PROCESS</h2><p>Filters are collected and transported back to the processing plant.</p></div>

<div class="abs step" style="left:87px;top:1544px">
  <svg width="44" height="48" viewBox="0 0 44 48" fill="none" stroke="var(--green)" stroke-width="4"><path d="M4 10h36M16 10V4h12v6M8 10l3 34h22l3-34M18 18v18M26 18v18"/></svg>
  <h3>Drained</h3><p>Excepteur sint occaecat cupidatat non proident, sunt in culpa qui officia deserunt mollit anim id est lasantium doloremqborum velit esse cill.</p></div>
<div class="abs divider" style="left:416px;top:1590px"></div>
<div class="abs step" style="left:443px;top:1544px">
  <svg width="48" height="50" viewBox="0 0 48 50" fill="none" stroke="var(--green)" stroke-width="5"><circle cx="20" cy="20" r="14"/><path d="M30 31l14 15"/></svg>
  <h3>Sorted</h3><p>Excepteur sint occaecat cupidatat non proident, sunt in culpa qui officia deserunt mollit anim id est lasantium doloremqborum velit esse cill.</p></div>
<div class="abs divider" style="left:766px;top:1590px"></div>
<div class="abs step" style="left:793px;top:1552px">
  <svg width="80" height="36" viewBox="0 0 80 36" fill="var(--green)"><rect x="2" y="6" width="50" height="20"/><path d="M54 12h14l10 10v6H54z"/><circle cx="16" cy="30" r="5"/><circle cx="64" cy="30" r="5"/></svg>
  <h3>Drained again</h3><p>Excepteur sint occaecat cupidatat non proident, sunt in culpa qui officia deserunt mollit anim id est lasantium doloremqborum velit esse cill.</p></div>

<div class="abs step" style="left:87px;top:1768px">
  <svg width="60" height="30" viewBox="0 0 60 30" fill="var(--green)"><rect x="0" y="0" width="18" height="8"/><rect x="21" y="0" width="18" height="8"/><rect x="42" y="0" width="18" height="8"/><rect x="0" y="11" width="8" height="8"/><rect x="11" y="11" width="18" height="8"/><rect x="32" y="11" width="18" height="8"/><rect x="53" y="11" width="7" height="8"/><rect x="0" y="22" width="18" height="8"/><rect x="21" y="22" width="18" height="8"/><rect x="42" y="22" width="18" height="8"/></svg>
  <h3>Crushed into bricks</h3><p>Excepteur sint occaecat cupidatat non proident, sunt in culpa qui officia deserunt mollit anim id est lasantium doloremqborum velit esse cill.</p></div>
<div class="abs divider" style="left:416px;top:1800px"></div>
<div class="abs step" style="left:443px;top:1756px">
  <svg width="56" height="52" viewBox="0 0 56 52" fill="none" stroke="var(--green)" stroke-width="5"><path d="M8 50V18a10 10 0 0 1 20 0v14a8 8 0 0 0 16 0V4"/><path d="M38 4h12"/></svg>
  <h3>Drained a third time</h3><p>Excepteur sint occaecat cupidatat non proident, sunt in culpa qui officia deserunt mollit anim id est lasantium doloremqborum velit esse cill.</p></div>
<div class="abs divider" style="left:766px;top:1800px"></div>
<div class="abs step" style="left:793px;top:1758px">
  <svg width="50" height="46" viewBox="0 0 50 46" fill="none" stroke="var(--green)" stroke-width="5"><path d="M18 8l7-5 7 5 6 10M42 26l4 8-4 8H30M20 42H8l-5-8 5-9"/><path d="M34 14l4 4 5-2M26 38l4 4-4 4M10 28l-2-4-5 1" stroke-width="3"/></svg>
  <h3>Stacked ready for<br>metal recycling</h3><p>Excepteur sint occaecat cupidatat non proident, sunt in culpa qui officia deserunt mollit anim id est</p></div>

<section class="abs reviews">
  <h2>OUR CUSTOMERS SAY</h2>
  <div class="card" style="left:98px">
    <div class="avatar" role="img" aria-label="Customer portrait"></div>
    <div class="who">Veritatis et<br><em>quasi beatae</em></div>
    <div class="badge" style="background:var(--navy)">ON CHATTERLY</div>
    <div class="txt">Each used oil filter has on aver age, more than quarter of a litre of used motor oil</div>
    <div class="meta">Like &nbsp;|&nbsp; Share &nbsp;|&nbsp; Comments</div>
  </div>
  <div class="card" style="left:442px">
    <div class="avatar" role="img" aria-label="Customer portrait"></div>
    <div class="who">Harlan P. Moss<br><em>President</em></div>
    <div class="badge" style="background:var(--red)">ON SEARCHLY</div>
    <div class="txt">Recycling engine oil protects the environment and conser ves energy resources</div>
    <div class="meta">Like &nbsp;|&nbsp; Share &nbsp;|&nbsp; Comments &nbsp;|&nbsp; 23 hours ago</div>
  </div>
  <div class="card" style="left:784px">
    <div class="avatar" role="img" aria-label="Customer portrait"></div>
    <div class="who">Darcy L.<br><em>Taylor CEO</em></div>
    <div class="badge" style="background:var(--navy)">ON CHATTERLY</div>
    <div class="txt">one litre of used oil can contaminate one million litres of water</div>
    <div class="meta">Like &nbsp;|&nbsp; Share &nbsp;|&nbsp; Comments</div>
  </div>
</section>
<div class="arrow" style="left:40px"></div>
<div class="arrow" style="left:1122px"></div>

<svg class="abs footer" viewBox="0 0 1200 530">
  <polygon points="0,85 600,0 1200,85 1200,530 0,530" fill="var(--footer)"/>
  <polygon points="0,78 600,0 1200,78 1200,88 600,12 0,88" fill="var(--green)"/>
</svg>
<div class="abs footer-body" role="img" aria-label="Dark background of stacked used filters" style="background:linear-gradient(#1a1a1a,#0d0d0d)"></div>

<div class="abs col contact" style="left:98px;top:2606px">
  <h4>CONTACT INFO</h4>
  <ul>
    <li><i><svg width="14" height="16" viewBox="0 0 14 16"><path d="M7 0a6 6 0 0 0-6 6c0 4 6 10 6 10s6-6 6-10a6 6 0 0 0-6-6z" fill="#fff"/><circle cx="7" cy="6" r="2" fill="#111"/></svg></i>Grennick Waste Partners Ltd<br>quis nostrum exercitationem ullam</li>
    <li><i><svg width="14" height="14" viewBox="0 0 14 14"><path d="M3 0l3 3-2 2c1 2 3 4 5 5l2-2 3 3-2 3C6 14 0 8 0 3z" fill="#fff"/></svg></i>Phone: &nbsp;06 555 0142</li>
    <li><i><svg width="16" height="16" viewBox="0 0 16 16" fill="none" stroke="#fff" stroke-width="2"><circle cx="8" cy="8" r="6"/><path d="M8 4v4l3 2"/></svg></i>Mo - Fr: 7.30am - 5.00pm</li>
    <li><i><svg width="16" height="12" viewBox="0 0 16 12"><rect width="16" height="12" rx="1" fill="#fff"/><path d="M0 1l8 6 8-6" fill="none" stroke="#111" stroke-width="1.5"/></svg></i>Email : info@grennickwaste.co.nz</li>
  </ul>
</div>
<div class="abs col links" style="left:394px;top:2606px">
  <h4>QUICK LINKS</h4>
  <ul><li>Home</li><li>About us</li><li>Gallery</li><li>Blog</li><li>Testimonials</li><li>Contact us</li></ul>
</div>
<div class="abs col news" style="left:564px;top:2606px">
  <h4>NEWSLETTER</h4>
  <p>Lorem Ipsum is simply dummy text of the printing</p>
  <div class="field">Enter Email</div>
  <div class="sub">SUBSCRIBE</div>
</div>
<div class="abs foot-brand"><i></i>Grennick Waste Partners</div>
<div class="abs social" style="left:886px;top:2718px">
  <i style="background:#2d4a8a"></i><i style="background:#2a9fd8"></i><i style="background:#e52d27"></i><i style="background:#1a6fa8"></i><i style="background:#e53a2e"></i>
</div>
<div class="abs rule"></div>
<div class="abs copy">Copyright © 2017 Grennick Waste Partners Ltd. All rights reserved.</div>
</body>
</html>
```